Business card design for Allied Healthcare provider

We would like a design for front and back of business cards. The design must resonate with all levels of customers from patients, to other health providers and medical. Must also resonate with corporate customers

Target Market(s)

patients, medical practitioners, other health providers and corporate.

Industry/Entity Type

healthcare

Contact Information for Business Card

name, logo, phone and fax numbers, email, website

Requirements
Must have
• not allowing me to change this, but the card must be double sided!! Please take note
Nice to have
• a fresh yet bold design to catch attention.

```html
<!DOCTYPE html>
<html lang="en">
<head>
<meta charset="utf-8">
<title>vitalcrest business card – front and back</title>
<link rel="stylesheet" href="https://fonts.googleapis.com/css2?family=Poppins:wght@500;600;700&family=Arimo:wght@400&display=swap">
<style>
  :root {
    --navy: #172a5e;
    --navy-deep: #13234f;
    --gold: #f0b323;
    --gold-edge: #c8961c;
    --white: #ffffff;
    --backdrop: #e6e6e4;
  }
  * { box-sizing: border-box; margin: 0; padding: 0; }
  html, body {
    width: 1200px;
    height: 801px;
    overflow: hidden;
    background: var(--backdrop);
  }
  .canvas {
    position: relative;
    width: 1200px;
    height: 801px;
    display: flex;
    align-items: center;
    justify-content: center;
    gap: 40px;
  }
  .card {
    position: relative;
    width: 540px;
    height: 310px;
    background: linear-gradient(160deg, var(--navy) 0%, var(--navy-deep) 100%);
    border-bottom: 4px solid var(--gold-edge);
    overflow: hidden;
    box-shadow: 0 12px 28px rgba(0, 0, 0, 0.22);
  }
  .brand {
    font-family: "Poppins", sans-serif;
    line-height: 1;
  }
  .brand-name {
    display: flex;
    align-items: center;
    gap: 10px;
    font-weight: 600;
    color: var(--white);
  }
  .brand-dot {
    flex: none;
    border-radius: 50%;
    background: var(--gold);
  }
  .brand-tagline {
    font-weight: 600;
    color: var(--gold);
    white-space: nowrap;
  }

  /* front: contact side */
  .card-front .brand { position: absolute; left: 36px; top: 38px; }
  .card-front .brand-name { font-size: 34px; }
  .card-front .brand-dot { width: 18px; height: 18px; }
  .card-front .brand-tagline { font-size: 13px; margin: 6px 0 0 28px; }

  .person { position: absolute; left: 64px; top: 140px; }
  .person-name {
    font-family: "Poppins", sans-serif;
    font-weight: 700;
    font-size: 22px;
    color: var(--gold);
  }
  .person-role {
    font-family: "Arimo", sans-serif;
    font-size: 14px;
    color: var(--white);
    margin-top: 2px;
  }

  .contact-list {
    position: absolute;
    left: 64px;
    top: 206px;
    list-style: none;
    font-family: "Arimo", sans-serif;
    font-size: 14px;
    color: var(--white);
  }
  .contact-list li {
    display: flex;
    align-items: center;
    gap: 10px;
    height: 20px;
  }
  .contact-icon { width: 13px; height: 13px; flex: none; }

  .address {
    position: absolute;
    right: 34px;
    top: 120px;
    text-align: right;
    font-family: "Arimo", sans-serif;
    font-size: 14px;
    line-height: 1.35;
    color: var(--white);
  }

  .edge-tab {
    position: absolute;
    left: 0;
    top: 230px;
    width: 10px;
    height: 34px;
    background: var(--gold);
  }

  /* back: brand side */
  .card-back .brand {
    position: absolute;
    left: 50%;
    top: 50%;
    transform: translate(-50%, -50%);
  }
  .card-back .brand-name { font-size: 44px; }
  .card-back .brand-dot { width: 24px; height: 24px; }
  .card-back .brand-tagline { font-size: 16px; margin: 8px 0 0 36px; }
</style>
</head>
<body>
<main class="canvas">

  <section class="card card-front" aria-label="Business card front">
    <div class="brand">
      <div class="brand-name"><span class="brand-dot"></span>vitalcrest</div>
      <div class="brand-tagline">care · comfort · wellness</div>
    </div>

    <div class="person">
      <div class="person-name">Daniel Harper</div>
      <div class="person-role">Manager</div>
    </div>

    <ul class="contact-list">
      <li>
        <svg class="contact-icon" viewBox="0 0 16 16" aria-label="Phone"><path d="M3 1.5l3 .2 1 3.3-1.8 1.3a9 9 0 0 0 4.5 4.5l1.3-1.8 3.3 1 .2 3c-6.5.8-12.3-5-11.5-11.5z" fill="#f0b323"/></svg>
        555-310-4820
      </li>
      <li>
        <svg class="contact-icon" viewBox="0 0 16 16" aria-label="Fax"><rect x="4" y="1" width="8" height="5" fill="#f0b323"/><rect x="1" y="6" width="14" height="8" rx="1.5" fill="#f0b323"/><rect x="4" y="9" width="8" height="2" fill="#172a5e"/></svg>
        555-310-4820
      </li>
      <li>
        <svg class="contact-icon" viewBox="0 0 16 16" aria-label="Email"><rect x="1" y="3" width="14" height="10" rx="1" fill="none" stroke="#f0b323" stroke-width="1.6"/><path d="M1.5 3.5L8 9l6.5-5.5" fill="none" stroke="#f0b323" stroke-width="1.6"/></svg>
        hello@vitalcrest.com
      </li>
      <li>
        <svg class="contact-icon" viewBox="0 0 16 16" aria-label="Website"><circle cx="8" cy="8" r="6.5" fill="none" stroke="#f0b323" stroke-width="1.5"/><ellipse cx="8" cy="8" rx="2.8" ry="6.5" fill="none" stroke="#f0b323" stroke-width="1.2"/><path d="M1.5 8h13M2.5 5h11M2.5 11h11" stroke="#f0b323" stroke-width="1"/></svg>
        www.vitalcrest.com
      </li>
    </ul>

    <p class="address">42 Harbor Lane, Easton<br>NY 12804</p>

    <div class="edge-tab" aria-hidden="true"></div>
  </section>

  <section class="card card-back" aria-label="Business card back">
    <div class="brand">
      <div class="brand-name"><span class="brand-dot"></span>vitalcrest</div>
      <div class="brand-tagline">care · comfort · wellness</div>
    </div>
  </section>

</main>
</body>
</html>
```